Sensual cosmetic range, design logo and box

This is a new sub brand under the Velarisse Range of cosmetics. Velarisse is a "Glow from the Core" range of approx 30 existing products.

This new range will consist of four products initially. I am seeking an innovative look and feel for this new sub brand of sensual cosmetics products. I have uploaded two pdfs of the box for the designs to be done on . I would like the designer to design the look and feel, colours etc and name of the range (all we have is the word sensual so the designer can use that name or it can be a entirely new name as long as it portrays the word sensual in it"

This particular product is sensual massage cream. I have supplied the box dimension on the pdf( one square and one rectangular.)

Target Market(s)

female only, between the ages of 24 to 49

Industry/Entity Type

Cosmetics

Requirements
Must have
• A name and design for the new range plus colours. Currently all we have is the name "sensuals". I am not stuck on this name and we are happy to see a new name. As long as the name, design and colour portrays " sensual or sensuality "

I have also supplied the existing Velarisse logo. I will leave it up to the designer interpretation if they want the existing velarisse logo to dominate or it can be made small and not prominent at all. it can even be made black and white .

the right colour combination. The containers I am using and packaging is all white, silver and clear. the box should go with these colours and also have a senual look and feel

keep in mind it is a women's range only

```html
<!DOCTYPE html>
<html lang="en">
<head>
<meta charset="utf-8">
<title>Velarisse Sensual Massage Cream</title>
<link rel="stylesheet" href="https://fonts.googleapis.com/css2?family=Didact+Gothic&family=Josefin+Sans:wght@100;300&display=swap">
<style>
  :root {
    --brand-pink: #e2288c;
    --soft-pink: #f3a3c7;
    --rose-text: #d979a8;
    --lavender: #a79bd3;
    --water-deep: #4f86d6;
    --water-light: #cfe2f7;
    --paper: #ffffff;
    --box-side: #f4f4f7;
    --fine-text: #b06a8e;
  }
  * { margin: 0; padding: 0; box-sizing: border-box; }
  html, body { width: 1200px; height: 900px; overflow: hidden; background: var(--paper); }
  .board {
    position: relative;
    width: 1200px;
    height: 900px;
    overflow: hidden;
    background: linear-gradient(180deg, #ffffff 0%, #f6f9fd 45%, #ffffff 100%);
    font-family: "Didact Gothic", "Helvetica Neue", Arial, sans-serif;
  }
  .water-splash { position: absolute; left: 0; top: 380px; width: 1200px; height: 330px; }
  .base-wave { position: absolute; left: 0; top: 700px; width: 1200px; height: 200px; }

  .brand { position: absolute; left: 62px; top: 52px; }
  .brand-name {
    display: flex; align-items: center; gap: 14px;
    color: var(--brand-pink);
    font-size: 68px; line-height: 1; letter-spacing: 1px;
  }
  .brand-dot { width: 40px; height: 40px; border-radius: 50%; background: var(--brand-pink); }
  .brand-tagline { margin-top: 44px; color: var(--brand-pink); font-size: 33px; }

  .range-title { position: absolute; left: 68px; top: 478px; }
  .range-name {
    font-family: "Josefin Sans", "Helvetica Neue", Arial, sans-serif;
    font-weight: 100;
    font-size: 122px; line-height: 1; letter-spacing: 2px;
    background: linear-gradient(180deg, var(--lavender) 0%, #c7a6d6 55%, var(--soft-pink) 100%);
    -webkit-background-clip: text; background-clip: text; color: transparent;
  }
  .range-product {
    margin-top: 2px; color: var(--rose-text);
    font-size: 52px; letter-spacing: 9px; line-height: 1;
  }

  .pack { position: absolute; left: 705px; top: 110px; display: flex; }
  .pack-front {
    position: relative; width: 285px; height: 565px;
    background: var(--paper); border: 1px solid #ececf2;
  }
  .pack-front .pack-brand {
    position: absolute; left: 14px; top: 30px;
    display: flex; align-items: center; gap: 8px;
    color: var(--brand-pink); font-size: 34px; line-height: 1;
  }
  .pack-front .pack-dot { width: 20px; height: 20px; border-radius: 50%; background: var(--brand-pink); }
  .pack-front .pack-tagline {
    position: absolute; left: 14px; top: 98px;
    color: var(--brand-pink); font-size: 20px;
  }
  .pack-front .pack-range { position: absolute; left: 0; right: 0; top: 308px; text-align: center; }
  .pack-range-name {
    font-family: "Josefin Sans", "Helvetica Neue", Arial, sans-serif;
    font-weight: 100; font-size: 46px; line-height: 1; letter-spacing: 1px;
    background: linear-gradient(180deg, var(--lavender) 0%, var(--soft-pink) 100%);
    -webkit-background-clip: text; background-clip: text; color: transparent;
  }
  .pack-range-product { color: var(--rose-text); font-size: 20px; letter-spacing: 3px; }
  .pack-front .pack-band {
    position: absolute; left: 0; right: 0; bottom: 0; height: 155px;
    background: var(--soft-pink); border-top: 3px solid #e7e3ee;
  }
  .pack-volume {
    position: absolute; left: 0; right: 0; bottom: 16px; text-align: center;
    color: var(--fine-text); font-size: 11px; letter-spacing: 0.5px;
  }
  .pack-side {
    position: relative; width: 78px; height: 565px;
    background: var(--box-side); border: 1px solid #e6e6ee; border-left: none;
  }
  .pack-side .pack-band {
    position: absolute; left: 0; right: 0; bottom: 0; height: 155px;
    background: #eb97bd; border-top: 3px solid #e0dbe8;
  }
  .pack-side-name {
    position: absolute; left: 12px; top: 22px;
    writing-mode: vertical-rl;
    font-family: "Josefin Sans", "Helvetica Neue", Arial, sans-serif;
    font-weight: 300; font-size: 54px; line-height: 1; letter-spacing: 2px;
    color: var(--lavender);
  }
</style>
</head>
<body>
<main class="board">

  <svg class="water-splash" viewBox="0 0 1200 330" role="img" aria-label="Photographic splash of clear blue water flowing across the board">
    <defs>
      <linearGradient id="waterTone" x1="0" y1="0" x2="1" y2="0">
        <stop offset="0" stop-color="#dbe8f7" stop-opacity="0.6"/>
        <stop offset="0.45" stop-color="#8fb4e6" stop-opacity="0.75"/>
        <stop offset="1" stop-color="#3f7ad2" stop-opacity="0.85"/>
      </linearGradient>
    </defs>
    <path d="M0 40 C200 10 380 60 560 50 C760 40 900 5 1040 -10 L1200 -20 L1200 260 C1050 250 900 220 720 230 C520 240 300 215 0 200 Z" fill="url(#waterTone)"/>
  </svg>

  <svg class="base-wave" viewBox="0 0 1200 200" aria-hidden="true">
    <path d="M0 38 C260 10 520 8 760 24 C960 38 1100 40 1200 20 L1200 200 L0 200 Z" fill="#ffffff"/>
    <path d="M0 58 C260 32 520 28 760 42 C960 55 1100 58 1200 40 L1200 200 L0 200 Z" fill="var(--soft-pink)"/>
  </svg>

  <header class="brand">
    <div class="brand-name"><span>Velarisse</span><span class="brand-dot"></span></div>
    <p class="brand-tagline">Glow from the Core</p>
  </header>

  <section class="range-title">
    <h1 class="range-name">SENSUAL</h1>
    <p class="range-product">massage cream</p>
  </section>

  <section class="pack" aria-label="Carton artwork">
    <div class="pack-front">
      <div class="pack-brand"><span>Velarisse</span><span class="pack-dot"></span></div>
      <p class="pack-tagline">Glow from the Core</p>
      <div class="pack-range">
        <p class="pack-range-name">SENSUAL</p>
        <p class="pack-range-product">massage cream</p>
      </div>
      <div class="pack-band"><p class="pack-volume">6.8 oz / 200 ml</p></div>
    </div>
    <div class="pack-side">
      <p class="pack-side-name">SENSUAL</p>
      <div class="pack-band"></div>
    </div>
  </section>

</main>
</body>
</html>
```